Water Filtration Company Needs completely refreshed powerpoint.

****UPDATE: I really need this project finished by next Wednesday. So what Im going to do, is pick a winner Sunday night.. USA Central Standard time. I will then offer a minimum $100 tip if the project is done well, and available for download Wednesday at midnight, USA central standard time.

I need a new power point. The thing is 30 slides. I was anything with graphics redone, I want it themed, beautiful, and brought up to the 2020's not 1995 like it looks like right now.

There are two files I had to delete a bit out of. Im not good with graphics but i was able to erase what I wanted in AI, but only know how to save as a PDF. So there are 2 PDF's.
I numbered the files.
I also included the winners of the bizz card, and brochure contest. My lgo was done on here too. Just for refrence.

Target Market(s)

Middle Class home owners, who are health conscience per se.

Font styles to use
Serif
Sans Serif

Requirements
Must have
• Cover sheet page. Editable source files when the job is done, and a source file thats ready to go.
I need every picture swapped out with something similar, text redone, all the graphics redone, on ALL 30 slides. I want it to look amazing, modern, like all the beautiful work I get done on this site. Im your biggest fan!!!
The text and graphics look like its from 1995.
My unit is black now, not white.
I want there to be a theme to all the pages.
I WILL tip the winning designer. It is a lot of work, but I didn't need 50+ designs for the next package up.
Between pages 6-7, Id like a page talking about how you can go to brenvo.org/pipecheck to see whats still in your water after it is treated. Simply enter your zipcode and select your water company to see whats in your water. I have a video i put in the brief I had made that explains it. It also mentions it in the brochure.

Editable files so I can make changes I may over look.
Nice to have
• I like when my logo is behind color code #192841, or black, it doesnt look so great floating over a white background.
Use colors from my logo as well if you can.
Should not have
• My website, and emails, are just Quorvine.com, not quor vine water systems, I just use it in my logo.

```html
<!DOCTYPE html>
<html lang="en">
<head>
<meta charset="utf-8">
<title>Quorvine Presentation Slides</title>
<link href="https://fonts.googleapis.com/css2?family=Montserrat:wght@400;600;700;800&family=Open+Sans:wght@400;600&display=swap" rel="stylesheet">
<style>
:root{
  --page:#e4e5e7;
  --navy:#192841;
  --navy-deep:#0d1729;
  --navy-mid:#223659;
  --blue:#2f9be3;
  --blue-light:#7cc6f2;
  --white:#ffffff;
  --muted:#b7c4d8;
  --line:#3a5078;
}
*{box-sizing:border-box;margin:0;padding:0}
html,body{width:818px;height:1200px;overflow:hidden;background:var(--page)}
body{font-family:"Open Sans",sans-serif;color:var(--white)}
.deck{position:relative;width:818px;height:1200px}
.slide{position:absolute;width:384px;height:216px;overflow:hidden;
  background:radial-gradient(ellipse at 30% 40%,var(--navy-mid),var(--navy-deep) 75%);
  box-shadow:0 2px 6px rgba(0,0,0,.25)}
.col-a{left:15px}.col-b{left:419px}
.row-1{top:20px}.row-2{top:256px}.row-3{top:492px}.row-4{top:728px}.row-5{top:964px}
.brand{position:absolute;display:flex;align-items:center;gap:4px;font-family:"Montserrat",sans-serif;font-weight:700;font-size:11px;color:var(--white)}
.brand .dot{width:7px;height:7px;border-radius:50%;background:var(--blue)}
.brand.tl{left:14px;top:12px}.brand.tr{right:14px;top:12px}
.art{position:absolute}
h2{font-family:"Montserrat",sans-serif;font-weight:800;line-height:1.05;text-transform:uppercase}
h2 .accent{color:var(--blue)}
.kicker{font-family:"Montserrat",sans-serif;font-weight:700;font-size:9px;color:var(--blue);text-transform:uppercase;letter-spacing:.5px}
.small{font-size:5.5px;line-height:1.5;color:var(--muted)}
.list{list-style:none;font-size:5.5px;line-height:1.75;color:var(--white)}
.list li::before{content:"";display:inline-block;width:4px;height:4px;border-radius:50%;background:var(--blue);margin-right:4px;vertical-align:middle}
.rule{height:2px;width:30px;background:var(--blue);margin:5px 0}

/* cover */
.cover-title{position:absolute;left:22px;top:78px;width:150px}
.cover-title .lead{font-size:13px;color:var(--blue)}
.cover-title .main{font-size:12px}
/* family */
.family{background:var(--navy-deep)}
.family-text{position:absolute;left:18px;top:20px;width:160px}
.family-text h2{font-size:12px}
/* info boxes */
.flow-box{position:absolute;width:70px;height:70px;border:1px solid var(--blue-light);background:rgba(13,23,41,.7);
  display:flex;flex-direction:column;align-items:center;justify-content:center;text-align:center;font-family:"Montserrat",sans-serif;font-size:6px;font-weight:600;padding:4px}
.flow-box .ico{width:22px;height:22px;border-radius:50%;background:var(--blue);margin-bottom:5px}
/* safe circle */
.safe{position:absolute;left:205px;top:95px;width:58px;height:58px;border-radius:50%;background:var(--white);color:var(--navy);
  display:flex;flex-direction:column;align-items:center;justify-content:center;font-family:"Montserrat",sans-serif;font-weight:800;font-size:7px;border:3px solid var(--blue)}
.safe .big{font-size:13px}
/* hardness table */
.hard-table{position:absolute;left:240px;top:78px;width:124px;border-collapse:collapse;font-size:6px}
.hard-table th{background:var(--blue);color:var(--white);font-family:"Montserrat",sans-serif;padding:3px 4px;text-align:left}
.hard-table td{padding:3px 4px;border-bottom:1px solid var(--line);color:var(--white)}
.hard-table tr:nth-child(even) td{background:rgba(47,155,227,.12)}
/* chlorine icons */
.icon-ring{position:absolute;width:30px;height:30px;border-radius:50%;border:1.5px solid var(--blue);display:flex;align-items:center;justify-content:center;font-size:5px;font-family:"Montserrat",sans-serif;font-weight:600}
</style>
</head>
<body>
<div class="deck">

  <!-- 1 cover -->
  <section class="slide col-a row-1">
    <div class="brand tl"><span class="dot"></span>Quorvine</div>
    <div class="cover-title">
      <h2><span class="lead">Spring</span><br><span class="main">Quality Alkaline Water<br><span class="accent">At Every Tap</span></span></h2>
    </div>
    <div class="art" role="img" aria-label="Three black water filter units standing side by side" style="left:190px;top:16px;width:120px;height:150px;background:linear-gradient(90deg,#05080f,#2a3344 50%,#05080f)"></div>
    <div class="art" role="img" aria-label="Blue water splash at the base" style="left:0;bottom:0;width:384px;height:50px;background:linear-gradient(0deg,rgba(47,155,227,.55),rgba(47,155,227,0))"></div>
  </section>

  <!-- 2 family -->
  <section class="slide col-b row-1 family">
    <div class="brand tr"><span class="dot"></span>Quorvine</div>
    <div class="family-text">
      <div class="kicker">Are You</div>
      <h2>A Water Drinking Family</h2>
      <div class="rule"></div>
      <ul class="list">
        <li>Do you drink bottled water daily?</li>
        <li>Do you cook with tap water?</li>
        <li>Do your kids drink from the tap?</li>
        <li>Do you care about clean hydration?</li>
        <li>Do you shower in treated water?</li>
        <li>Do you want better tasting water?</li>
      </ul>
      <p class="small" style="margin-top:6px">If you answered yes, this is the right system for your home and family.</p>
    </div>
    <div class="art" role="img" aria-label="Slanted strip photos of family members drinking water" style="left:200px;top:34px;width:170px;height:120px;background:linear-gradient(120deg,#c9d3de,#8aa0b8 50%,#e8ecf0);clip-path:polygon(15% 0,100% 0,85% 100%,0 100%)"></div>
  </section>

  <!-- 3 product -->
  <section class="slide col-a row-2">
    <div class="brand tl"><span class="dot"></span>Quorvine</div>
    <div style="position:absolute;left:18px;top:48px;width:140px">
      <p class="small" style="color:var(--white)">Our filters deliver clean alkaline water straight from your tap.</p>
      <div class="rule"></div>
      <ul class="list">
        <li>Removes chlorine and lead</li>
        <li>Balances your water pH</li>
        <li>Adds healthy minerals</li>
        <li>Simple under sink install</li>
      </ul>
    </div>
    <div class="art" role="img" aria-label="Black filter unit above a splash of water" style="left:185px;top:20px;width:60px;height:150px;background:linear-gradient(90deg,#05080f,#2c3547 50%,#05080f);border-radius:6px"></div>
    <div class="art" role="img" aria-label="Water ripple surface" style="left:0;bottom:0;width:384px;height:55px;background:linear-gradient(0deg,rgba(47,155,227,.5),rgba(47,155,227,0))"></div>
  </section>

  <!-- 4 what's in your water -->
  <section class="slide col-b row-2">
    <div class="art" role="img" aria-label="Faded photo of a family kitchen" style="inset:0;background:linear-gradient(135deg,#3c4a5e,#1c273a)"></div>
    <div class="brand tr"><span class="dot"></span>Quorvine</div>
    <h2 style="position:absolute;left:0;right:0;top:40px;text-align:center;font-size:12px">What's In <span class="accent">Your Water?</span></h2>
    <div class="flow-box" style="left:90px;top:80px"><span class="ico"></span>Water enters your home<br>with contaminants</div>
    <svg class="art" style="left:168px;top:108px" width="40" height="14" viewBox="0 0 40 14"><path d="M0 7h34M28 1l8 6-8 6" stroke="#2f9be3" stroke-width="2" fill="none"/></svg>
    <div class="flow-box" style="left:214px;top:80px"><span class="ico"></span>And leaves<br>pure and alkaline</div>
  </section>

  <!-- 5 universal solvent -->
  <section class="slide col-a row-3">
    <div class="brand tl"><span class="dot"></span>Quorvine</div>
    <div class="art" role="img" aria-label="Illustrated water cycle with clouds, mountains and land" style="left:18px;top:34px;width:150px;height:100px;background:linear-gradient(180deg,#9fd4f2,#5c9c58 70%,#3a6c8a)"></div>
    <div style="position:absolute;left:20px;top:145px;width:220px">
      <h2 style="font-size:12px">Water Is<br><span class="accent">The Universal Solvent</span></h2>
      <p class="small" style="margin-top:4px">A single molecule dissolves more substances than any other liquid. That means it carries them into your home.</p>
    </div>
  </section>

  <!-- 6 what happens -->
  <section class="slide col-b row-3">
    <div class="art" role="img" aria-label="Photo of water running from a kitchen faucet into a glass" style="left:0;top:0;width:175px;height:216px;background:linear-gradient(160deg,#d8dde3,#6f7c8e)"></div>
    <div class="brand tr"><span class="dot"></span>Quorvine</div>
    <h2 style="position:absolute;left:240px;top:34px;width:130px;font-size:8px">What Happens To Your Water <span class="accent">Before It Gets To Your Home?</span></h2>
    <div class="safe"><span>Is Your Water</span><span class="big">Safe?</span></div>
    <ul class="list" style="position:absolute;left:275px;top:80px">
      <li>Chlorine</li><li>Fluoride</li><li>Lead</li><li>Arsenic</li><li>Nitrates</li><li>Bacteria</li>
    </ul>
    <ul class="list" style="position:absolute;left:325px;top:80px">
      <li>Pesticides</li><li>Mercury</li><li>Copper</li><li>Radium</li><li>Sulfates</li><li>Chloramine</li>
    </ul>
  </section>

  <!-- 7 water treatment -->
  <section class="slide col-a row-4">
    <div class="art" role="img" aria-label="Technical illustration of a municipal water treatment plant" style="left:10px;top:12px;width:230px;height:190px;background:linear-gradient(180deg,#f3f6f9,#b8d4e8)"></div>
    <div class="brand tr"><span class="dot"></span>Quorvine</div>
    <div style="position:absolute;left:255px;top:90px;width:115px">
      <h2 style="font-size:12px">Water<br><span class="accent">Treatment</span></h2>
      <p class="small" style="margin-top:4px">Municipal plants treat water with chemicals, but many contaminants still remain.</p>
    </div>
  </section>

  <!-- 8 test your tap water -->
  <section class="slide col-b row-4">
    <div class="art" role="img" aria-label="Photo of a glass being filled with tap water" style="left:0;top:0;width:150px;height:216px;background:linear-gradient(180deg,#c8d0d8,#4f5d70)"></div>
    <div class="brand tr"><span class="dot"></span>Quorvine</div>
    <div style="position:absolute;left:175px;top:55px;display:flex;align-items:center;gap:6px">
      <span style="width:26px;height:26px;border-radius:50%;background:var(--white)"></span>
      <h2 style="font-size:12px">Test Your <span class="accent">Tap Water</span></h2>
    </div>
    <p class="small" style="position:absolute;left:175px;top:95px;width:180px">Visit brenvo.org/pipecheck, enter your zipcode and select your water company.</p>
  </section>

  <!-- 9 hardness -->
  <section class="slide col-a row-5">
    <div class="brand tl"><span class="dot"></span>Quorvine</div>
    <h2 style="position:absolute;left:18px;top:32px;font-size:12px">How Hard Is <span class="accent">Your Water?</span></h2>
    <p class="small" style="position:absolute;left:18px;top:50px;width:210px">Hard water leaves scale on fixtures and dries your skin and hair.</p>
    <div class="art" role="img" aria-label="Map of the United States shaded by water hardness" style="left:18px;top:78px;width:205px;height:120px;background:linear-gradient(135deg,#8fd0f5,#2f6fb5 60%,#123a78)"></div>
    <table class="hard-table">
      <tr><th>Hardness</th><th>GPG</th></tr>
      <tr><td>Soft</td><td>0-1</td></tr>
      <tr><td>Slightly</td><td>1-3.5</td></tr>
      <tr><td>Moderate</td><td>3.5-7</td></tr>
      <tr><td>Hard</td><td>7-10.5</td></tr>
      <tr><td>Very Hard</td><td>10.5+</td></tr>
    </table>
  </section>

  <!-- 10 chlorine -->
  <section class="slide col-b row-5">
    <div class="brand tl"><span class="dot"></span>Quorvine</div>
    <h2 style="position:absolute;left:18px;top:38px;font-size:12px">The Dangers <span class="accent">Of Chlorine</span></h2>
    <p class="small" style="position:absolute;left:18px;top:58px;width:190px">Chlorine is added to kill bacteria but it reacts with organic matter. Skin, hair and lungs absorb it in the shower.</p>
    <div class="icon-ring" style="left:40px;top:100px">Skin</div>
    <div class="icon-ring" style="left:80px;top:100px">Hair</div>
    <div class="icon-ring" style="left:120px;top:100px">Lungs</div>
    <div class="icon-ring" style="left:160px;top:100px">Eyes</div>
    <div class="art" role="img" aria-label="Photo of a woman holding her head in discomfort" style="left:250px;top:0;width:134px;height:216px;background:linear-gradient(180deg,#e9e6e2,#c3b8ad)"></div>
  </section>

</div>
</body>
</html>
```